K7 Website Project

We need a web design for our new company K7. We just decided on our company brand. I will upload our company brand for you to use in the web design. We want a powerful few statements to catch the eye of the browser. Our company is being founded to protect elementary schools, junior high schools and high schools against predators that want to harm children. We are going to employ veterans and police officers, only. Superintendents of schools, principals of schools will be viewing this site. This site needs to be thoughtful and impactful to the current needs of school districts. We will have a couple testimonials that will be included on the site.
Updates

We need this website as soon as possible.  We added more information.

Target Market(s)

School districts

Industry/Entity Type

School

Requirements
Must have
• Website must have logo and brand. Area for contact information. Links to take the user to learn more about the company, testimonials, frequently asked questions, contact information
Should not have
• Should not be too busy, simple but classy.

```html
<!DOCTYPE html>
<html lang="en">
<head>
<meta charset="utf-8">
<title>K7 – Keep Safe</title>
<link rel="stylesheet" href="https://fonts.googleapis.com/css2?family=Questrial&family=Noto+Sans:wght@400;500&display=swap">
<style>
  :root {
    --page-bg: #000000;
    --bar-dark: #2b2b2b;
    --header-strip: rgba(58, 58, 58, 0.78);
    --panel-grey: #e0dfe0;
    --panel-white: #ffffff;
    --footer-grey: #9c9c9c;
    --text-dark: #111111;
    --text-muted: #555555;
    --nav-text: #f2f2f2;
    --brand-gold: #c9a24a;
    --photo-deep: #0b1626;
    --photo-navy: #1b2f4a;
    --photo-mid: #4f8aa3;
    --photo-light: #c9dde4;
  }
  * { margin: 0; padding: 0; box-sizing: border-box; }
  html, body { width: 1200px; height: 1000px; overflow: hidden; background: var(--page-bg); }
  body { position: relative; font-family: "Noto Sans", sans-serif; color: var(--text-dark); }

  .site { position: absolute; left: 148px; top: 0; width: 900px; height: 1000px; }

  /* Header */
  .header { position: absolute; left: 0; top: 0; width: 900px; height: 307px; background: var(--page-bg); overflow: hidden; }
  .header-photo { position: absolute; left: 330px; top: 0; width: 570px; height: 307px;
    background:
      linear-gradient(90deg, var(--page-bg) 0%, rgba(0,0,0,0.85) 14%, rgba(0,0,0,0) 40%),
      radial-gradient(ellipse 70% 60% at 62% 55%, var(--photo-light) 0%, var(--photo-mid) 38%, rgba(79,138,163,0) 70%),
      linear-gradient(180deg, #8aa6b6 0%, var(--photo-navy) 28%, var(--photo-deep) 100%); }
  .header-strip { position: absolute; left: 0; top: 0; width: 900px; height: 65px; background: var(--header-strip); }
  .tagline { position: absolute; left: 89px; top: 17px; font-family: "Questrial", sans-serif; font-size: 31px; color: #e8e8e8; letter-spacing: .5px; }
  .brand { position: absolute; left: 92px; top: 108px; display: flex; align-items: center; gap: 16px; }
  .brand-mark { width: 30px; height: 30px; border-radius: 50%; background: var(--brand-gold); }
  .brand-name { font-family: "Questrial", sans-serif; font-size: 118px; color: var(--brand-gold); line-height: 1; }

  /* Navigation */
  .main-nav { position: absolute; left: 0; top: 307px; width: 900px; height: 64px; background: var(--bar-dark); }
  .main-nav a { position: absolute; top: 0; font-family: "Questrial", sans-serif; font-size: 19px; letter-spacing: -0.3px; color: var(--nav-text); text-decoration: none; line-height: 72px; white-space: nowrap; }
  .main-nav a.is-active { left: 0; width: 152px; padding-left: 34px; background: var(--panel-grey); color: var(--text-dark); }

  /* Why choose us */
  .why { position: absolute; left: 0; top: 371px; width: 900px; height: 386px; background: var(--panel-grey); }
  .why h1 { position: absolute; left: 13px; top: 37px; font-weight: 400; font-size: 28px; letter-spacing: 1px; }
  .team-photo { position: absolute; left: 11px; top: 90px; width: 380px; height: 270px; border: 2px solid #fff;
    background: linear-gradient(180deg, #3d5a3a 0%, #6b7a6a 45%, #9a9a96 75%, #b4b4b0 100%); }
  .why-copy { position: absolute; left: 401px; top: 100px; width: 485px; font-size: 14.2px; letter-spacing: 0.35px; line-height: 16.7px; }
  .why-copy p + p { margin-top: 16.7px; }

  /* Highlights */
  .highlights { position: absolute; left: 0; top: 757px; width: 900px; height: 193px; background: var(--panel-white); }
  .highlight { position: absolute; top: 18px; }
  .highlight h2 { font-weight: 400; font-size: 23px; letter-spacing: .5px; line-height: 28px; margin-bottom: 8px; }
  .highlight p { font-size: 14.2px; letter-spacing: 0.35px; line-height: 16.7px; }
  .highlight p + p { margin-top: 16.7px; }
  .more { position: absolute; top: 155px; font-size: 14px; color: var(--text-muted); letter-spacing: 1px; text-decoration: none; }
  .h-about { left: 10px; width: 245px; }
  .h-services { left: 320px; width: 250px; }
  .h-testimonials { left: 649px; width: 250px; }

  /* Footer */
  .footer-band { position: absolute; left: 0; top: 950px; width: 1200px; height: 50px; background: var(--bar-dark); }
  .footer { position: absolute; left: 0; top: 950px; width: 900px; height: 50px; background: var(--footer-grey); text-align: center; }
  .footer-nav { display: flex; justify-content: center; gap: 15px; padding-top: 13px; }
  .footer-nav a { font-family: "Questrial", sans-serif; font-size: 11px; color: var(--text-dark); text-decoration: none; }
  .copyright { font-size: 11.5px; margin-top: 9px; }
</style>
</head>
<body>
  <div class="footer-band"></div>
  <div class="site">
    <header class="header">
      <div class="header-photo" role="img" aria-label="Security officer watching a row of surveillance monitors"></div>
      <div class="header-strip"></div>
      <div class="tagline">KEEP SAFE</div>
      <div class="brand">
        <span class="brand-mark"></span>
        <span class="brand-name">K7</span>
      </div>
    </header>

    <nav class="main-nav">
      <a class="is-active" href="#">COMPANY</a>
      <a style="left:163px" href="#">SERVICES</a>
      <a style="left:275px" href="#">SUPPORT</a>
      <a style="left:385px" href="#">CLIENTS</a>
      <a style="left:483px" href="#">TESTIMONIALS</a>
      <a style="left:639px" href="#">QUESTIONS</a>
      <a style="left:769px" href="#">CONTACT</a>
    </nav>

    <section class="why">
      <h1>WHY CHOOSE US ?</h1>
      <div class="team-photo" role="img" aria-label="Security team in white shirts standing together on a street"></div>
      <div class="why-copy">
        <p>Lorem ipsum dolor sit amet, consectetuer adipiscing elit, sed diam nonummy nibh euismod tincidunt ut laoreet dolore magna aliquam erat volutpat. Ut wisi enim ad minim veniam, quis nostrud exerci tation ullamcorper suscipit lobortis nisl ut aliquip ex ea commodo consequat.</p>
        <p>Lorem ipsum dolor sit amet, consectetuer adipiscing elit, sed diam nonummy nibh euismod tincidunt ut laoreet dolore magna aliquam erat volutpat. Ut wisi enim ad minim veniam, quis nostrud exerci tation ullamcorper suscipit lobortis nisl ut aliquip ex ea commodo consequat. Lorem ipsum dolor sit amet, consectetuer adipiscing elit, sed diam nonummy nibh euismod tincidunt ut laoreet dolore magna aliquam erat volutpat. Ut wisi enim ad minim veniam, quis nostrud exerci tation ullamcorper suscipit lobortis nisl ut aliquip ex ea commodo consequat.</p>
      </div>
    </section>

    <section class="highlights">
      <div class="highlight h-about">
        <h2>ABOUT US</h2>
        <p>Lorem ipsum dolor sit amet, consectetuer adipiscing elit, sed diam nonummy nibh euismod tincidunt ut laoreet dolore magna aliquam erat volutpat. Lorem ipsum dolor sit amet,</p>
      </div>
      <a class="more" style="left:177px" href="#">MORE&gt;&gt;</a>

      <div class="highlight h-services">
        <h2>OUR SERVICES</h2>
        <p>Lorem ipsum dolor sit amet, consectetuer adipiscing elit, sed</p>
        <p>Lorem ipsum dolor sit amet, consectetuer adipiscing elit, sed</p>
      </div>
      <a class="more" style="left:477px" href="#">MORE&gt;&gt;</a>

      <div class="highlight h-testimonials">
        <h2>TESTIMONIALS</h2>
        <p>“Lorem ipsum dolor sit amet, consectetuer adipiscing elit, sed”</p>
        <p>“Lorem ipsum dolor sit amet”</p>
      </div>
      <a class="more" style="left:811px" href="#">MORE&gt;&gt;</a>
    </section>

    <footer class="footer">
      <nav class="footer-nav">
        <a href="#">COMPANY</a>
        <a href="#">SERVICES</a>
        <a href="#">SUPPORT</a>
        <a href="#">CLIENTS</a>
        <a href="#">TESTIMONIALS</a>
        <a href="#">QUESTIONS</a>
        <a href="#">CONTACT</a>
      </nav>
      <p class="copyright">© Copyright K7 Company Inc 2004-2013</p>
    </footer>
  </div>
</body>
</html>
```